A4 Menu needed for cafe - attached design

Need an A4 menu designed for our cafe.
I have attached our catering menu - I would like the new menu to be designed in the exact same way.

I have attached the text that needs to appear on the menu

Industry/Entity Type

Catering

```html
<!DOCTYPE html>
<html lang="en">
<head>
<meta charset="UTF-8">
<title>Harbour Hall – Catering Menu</title>
<link rel="stylesheet" href="https://fonts.googleapis.com/css2?family=Arvo:wght@400;700&family=Pathway+Gothic+One&family=Lato:wght@400&display=swap">
<style>
  :root {
    --board: #111213;
    --board-light: #1b1c1e;
    --chalk: #ffffff;
    --chalk-soft: #dcdcdc;
    --highlight: #f6f77e;
    --ink: #231f22;
  }
  * { margin: 0; padding: 0; box-sizing: border-box; }
  html, body { width: 1200px; height: 849px; overflow: hidden; }
  body {
    position: relative;
    background: radial-gradient(ellipse at 50% 40%, var(--board-light) 0%, var(--board) 75%);
    color: var(--chalk);
    font-family: "Arvo", Georgia, serif;
  }

  .brand {
    position: absolute; left: 535px; top: 19px; width: 129px; height: 111px;
    background: var(--highlight);
    display: flex; align-items: center; justify-content: center;
    font-family: "Arvo", Georgia, serif; font-weight: 400;
    font-size: 17px; letter-spacing: 1px; line-height: 1.2;
    color: var(--ink); text-align: center; text-transform: uppercase;
  }
  .brand-tagline {
    position: absolute; left: 0; width: 1200px; top: 139px;
    text-align: center; color: var(--highlight);
    font-family: "Arvo", Georgia, serif; font-size: 18px;
  }

  .menu-section {
    position: absolute;
    border: 2px solid var(--chalk);
  }
  .section-breakfast { left: 91px; top: 209px; width: 485px; height: 323px; }
  .section-lunch { left: 624px; top: 209px; width: 485px; height: 323px; }
  .section-light { left: 91px; top: 583px; width: 1018px; height: 207px; }

  .section-banner {
    position: absolute; width: 352px; height: 48px;
  }
  .section-banner svg { position: absolute; inset: 0; }
  .section-banner h2 {
    position: relative; z-index: 1;
    font-family: "Pathway Gothic One", "Arial Narrow", sans-serif;
    font-weight: 400; font-size: 27px; letter-spacing: 0.5px;
    line-height: 48px; text-align: center; color: var(--chalk);
  }
  .section-breakfast .section-banner,
  .section-lunch .section-banner { left: 66px; top: -25px; }
  .section-light .section-banner { left: 68px; top: -24px; }

  .item-list {
    position: absolute; list-style: none;
    width: 416px;
  }
  .section-breakfast .item-list,
  .section-lunch .item-list { left: 32px; top: 36px; }
  .item-list.col-left { left: 32px; top: 43px; }
  .item-list.col-right { left: 565px; top: 18px; }

  .item {
    display: flex; justify-content: space-between;
    font-weight: 700; font-size: 17px; line-height: 24.7px;
    letter-spacing: 0.1px;
  }

  .contact-line {
    position: absolute; left: 0; width: 1200px; top: 813px;
    text-align: center; font-family: "Lato", Arial, sans-serif;
    font-size: 12.5px; color: var(--chalk-soft);
  }
</style>
</head>
<body>

  <div class="brand">Harbour<br>Hall</div>
  <p class="brand-tagline">catering menu</p>

  <section class="menu-section section-breakfast">
    <div class="section-banner">
      <svg viewBox="0 0 352 48" aria-hidden="true"><polygon points="2,2 350,2 332,24 350,46 2,46 20,24" fill="var(--board)" stroke="var(--highlight)" stroke-width="3"/></svg>
      <h2>BREAKFAST</h2>
    </div>
    <ul class="item-list">
      <li class="item"><span>toast</span><span>$2.0</span></li>
      <li class="item"><span>raisin toast</span><span>$2.0</span></li>
      <li class="item"><span>egg bacon and cheese roll</span><span>$6.5</span></li>
      <li class="item"><span>veggie brekky wrap</span><span>$6.5</span></li>
      <li class="item"><span>ham and cheese french toast</span><span>$6.5</span></li>
      <li class="item"><span>ham and cheese toastie</span><span>$5.5</span></li>
      <li class="item"><span>cheese and tomato toastie</span><span>$5.5</span></li>
      <li class="item"><span>ham and cheese croissant</span><span>$6.5</span></li>
      <li class="item"><span>cheese and tomato croissant</span><span>$6.0</span></li>
      <li class="item"><span>ham cheese and tomato toastie</span><span>$6.0</span></li>
      <li class="item"><span>plain croissant</span><span>$3.5</span></li>
    </ul>
  </section>

  <section class="menu-section section-lunch">
    <div class="section-banner">
      <svg viewBox="0 0 352 48" aria-hidden="true"><polygon points="2,2 350,2 332,24 350,46 2,46 20,24" fill="var(--board)" stroke="var(--highlight)" stroke-width="3"/></svg>
      <h2>LUNCH</h2>
    </div>
    <ul class="item-list">
      <li class="item"><span>pre made sandwiches</span><span>$6.5/$7.5</span></li>
      <li class="item"><span>pre made focaccias</span><span>$8.5</span></li>
      <li class="item"><span>pre made wraps</span><span>$7.5</span></li>
      <li class="item"><span>pre made mini rolls</span><span>$4.0</span></li>
      <li class="item"><span>pre made baguettes</span><span>$9.0</span></li>
      <li class="item"><span>pre made bagels</span><span>$9.0</span></li>
      <li class="item"><span>fresh salads made daily</span><span>$9.5</span></li>
      <li class="item"><span>hot chips</span><span>$4.5</span></li>
      <li class="item"><span>plain hamburger</span><span>$7.5</span></li>
      <li class="item"><span>hamburger with the lot</span><span>$9.0</span></li>
      <li class="item"><span>chicken schnitzel burger</span><span>$8.5</span></li>
    </ul>
  </section>

  <section class="menu-section section-light">
    <div class="section-banner">
      <svg viewBox="0 0 352 48" aria-hidden="true"><polygon points="2,2 350,2 332,24 350,46 2,46 20,24" fill="var(--board)" stroke="var(--highlight)" stroke-width="3"/></svg>
      <h2>SOMETHING LIGHT</h2>
    </div>
    <ul class="item-list col-left">
      <li class="item"><span>mixed yoghurts</span><span>$5.5</span></li>
      <li class="item"><span>granola and fruit yoghurt</span><span>$5.5</span></li>
      <li class="item"><span>chia pudding</span><span>$5.5</span></li>
      <li class="item"><span>bircher muesli</span><span>$5.5</span></li>
      <li class="item"><span>fruit salad</span><span>$5.5</span></li>
      <li class="item"><span>banana bread</span><span>$4.5</span></li>
    </ul>
    <ul class="item-list col-right">
      <li class="item"><span>muffins – made fresh daily</span><span>$4.5</span></li>
      <li class="item"><span>slices</span><span>$4.0</span></li>
      <li class="item"><span>cookies</span><span>$4.0</span></li>
      <li class="item"><span>choc crunch energy bite</span><span>$4.0</span></li>
      <li class="item"><span>super crunch energy bite</span><span>$4.0</span></li>
      <li class="item"><span>chocolate bar</span><span>$3.0</span></li>
      <li class="item"><span>packet of chips</span><span>$3.0</span></li>
    </ul>
  </section>

  <p class="contact-line">Visit us instore to discuss catering options, or call 0412 555 019 or email mia@harbourhallcanteen.com</p>

</body>
</html>
```